Electronic call to action mailer

I am launching my new web site and would like to send an electronic mailer to a segmented base. The base would be mostly mothers with children and I want them to shop at my new web site.

I would like to include a call to action - if they register as members they will get 20% off their first purchase and a 10% thereafter as members.

They will also be in a lucky draw contest for a $500 voucher to use at our wen site.
Updates

I have updated the details I require. As this is a call to action page, it should be really catchy that we brand new company that promises to bring quality children's products to them. The company's vision is pinned to producing and distributing organic products and products that are produced with fair trade practices.

Reason: I was late in updating my brief and I think there are a few designs that I already like. I just need to have the updates in

Target Market(s)

Parents that are interested in quality products for kids

Industry/Entity Type

Electronic

Font styles to use
Sans Serif

Colors
c1b2d3
86cfc6
f04a50

Requirements
Must have
• I page that is really easy to get the message. 5 consolation prizes that will be from the Tiny Amber Meadows toiletry range. (picture included). Winner gets $500 worth of goods (at RRP)
Must mention that this is in conjunction with the launch of our new on-line shop.
Must mention that our range of clothes are new to Singapore and we have exclusivity with the brands
terms and conditions apply
Nice to have
• A catchy tag line, making them want to become a member

```html
<!DOCTYPE html>
<html lang="en">
<head>
<meta charset="utf-8">
<title>Call to Action Mailer</title>
<link rel="stylesheet" href="https://fonts.googleapis.com/css2?family=Archivo+Black&family=Arimo:ital,wght@0,400;0,700;1,400&display=swap">
<style>
  :root {
    --paper: #ffffff;
    --ink: #1a1a1a;
    --lilac: #c1b2d3;
    --teal: #86cfc6;
    --coral: #f04a50;
    --panel-dark: #2f2f2f;
    --panel-light: #e9ebee;
  }
  * { margin: 0; padding: 0; box-sizing: border-box; }
  html, body { width: 1200px; height: 898px; overflow: hidden; background: var(--paper); }
  .canvas {
    position: relative; width: 1200px; height: 898px; background: var(--paper); color: var(--ink);
    font-family: "Arimo", sans-serif;
  }

  .title-art { position: absolute; left: 0; top: 0; }
  .title {
    position: absolute; left: 110px; top: 78px;
    font-family: "Arimo", sans-serif; font-weight: 400; font-size: 40px; letter-spacing: 8.5px;
    color: var(--ink); line-height: 1; white-space: nowrap;
  }

  .mailer-heading {
    position: absolute; left: 36px; top: 215px;
    font-family: "Archivo Black", sans-serif; font-weight: 400; font-size: 23px; letter-spacing: 4.6px;
    line-height: 1; white-space: nowrap;
  }
  .heading-rule { position: absolute; left: 15px; top: 257px; width: 843px; height: 3px; background: var(--ink); }

  .section-label {
    position: absolute; left: 36px;
    font-weight: 700; font-size: 15px; letter-spacing: 1.2px;
    color: var(--coral); line-height: 1; white-space: nowrap;
  }
  .label-launch { top: 276px; }
  .label-benefits { top: 589px; }

  .body-copy {
    position: absolute; left: 36px;
    font-size: 20px; line-height: 39.5px; white-space: nowrap;
  }
  .copy-launch { top: 306px; }
  .copy-benefits { top: 622px; }

  .dashboard-shot {
    position: absolute; left: 650px; top: 272px; width: 362px; height: 266px;
    background: linear-gradient(180deg, var(--panel-dark) 0 30px, var(--panel-light) 30px 100%);
  }

  .prompt {
    position: absolute; left: 780px; top: 632px;
    font-style: italic; font-size: 20px; line-height: 52.5px; white-space: nowrap;
  }

  .fine-print {
    position: absolute; left: 36px; top: 842px; width: 1130px;
    padding-top: 10px; border-top: 2px solid var(--teal);
    font-size: 13px; line-height: 20px; color: var(--ink);
  }
  .fine-print strong { color: var(--coral); font-weight: 700; }
</style>
</head>
<body>
<main class="canvas">
  <svg class="title-art" width="640" height="180" viewBox="0 0 640 180" aria-hidden="true">
    <defs>
      <linearGradient id="bandFade" x1="0" x2="1" y1="0" y2="0">
        <stop offset="0" stop-color="#c1b2d3"/>
        <stop offset="0.15" stop-color="#c1b2d3"/>
        <stop offset="1" stop-color="#ffffff"/>
      </linearGradient>
    </defs>
    <rect x="5" y="57" width="605" height="77" fill="url(#bandFade)"/>
    <circle cx="108" cy="93" r="79" fill="none" stroke="#86cfc6" stroke-width="1.5"/>
    <path d="M101 42 H90 V144 H101" fill="none" stroke="#1a1a1a" stroke-width="6"/>
    <path d="M608 42 H622 V144 H608" fill="none" stroke="#f04a50" stroke-width="6"/>
  </svg>
  <h1 class="title">CALL TO ACTION</h1>

  <h2 class="mailer-heading">CALL TO ACTION MAILER</h2>
  <div class="heading-rule"></div>

  <h3 class="section-label label-launch">LAUNCHING OF THE NEW WEBSITE</h3>
  <p class="body-copy copy-launch">I am welcoming you all to shop at our new web<br>site. It has all the goods and services you would<br>require. My target market is mothers who have<br>children since there are many products that&nbsp; would<br>satisfy family and children’s needs.</p>

  <div class="dashboard-shot" role="img" aria-label="Screenshot of the Nimbus Reach marketing dashboard with the Content menu open and an arrow pointing to Calls-to-Action"></div>

  <h3 class="section-label label-benefits">BENEFITS</h3>
  <p class="body-copy copy-benefits">However, the advantage is all yours because&nbsp; if you<br>register as members they will get 20% off&nbsp; you first<br>purchase and a 10% thereafter as members. Also<br>you will&nbsp; be in a lucky draw contest for a $500<br>voucher to use at our web site.</p>

  <p class="prompt">Lucky ones are those<br>that register first . Book<br>a form to be among the<br>winners.</p>

  <p class="fine-print">In conjunction with the launch of our new online shop. Our clothing brands are new to Singapore and exclusive to us. Winner gets $500 worth of goods (at RRP); <strong>5 consolation prizes</strong> from the Tiny Amber Meadows toiletry range. <strong>Terms and conditions apply.</strong></p>
</main>
</body>
</html>
```